Sleek Design For Personal Brand Wordpress Website !!

*WORDPRESS WEBSITE*

Need a sleek and easy to navigate Wordpress website.

It will act as the hub for my personal brand.

Which means it will showcase all my social media outlets, host my most recent content like youtube videos and podcasts...

It will also be the go to place to find all my digital products and services that I offer.

i want it to be super sleek and simple but also give a personal touch of my who I really am. You can get a good idea of who I am my checking out my Instagram (@karel.dumonte)

Use these websites for ideas: www.brevanhollis.example and www.dorianfelkowitz.example

Target Market(s)

Young Entrepreneurs

Industry/Entity Type

Education

Logo Text

Karel Dumonte

Number of Pages Required

4 page

Font styles to use
Sans Serif

Colors
ffffff
0392cd
ec1f27

Requirements
Must have
• Social Media buttons on the home page...
• Video (also a slider) right at the top of the home page...
• Email Optin...
• Multiple pages...

```html
<!DOCTYPE html>
<html lang="en">
<head>
<meta charset="utf-8">
<title>Karel Dumonte — Personal Brand</title>
<link href="https://fonts.googleapis.com/css2?family=Arimo:ital,wght@0,400;0,700;1,400;1,700&display=swap" rel="stylesheet">
<style>
  :root {
    --white: #ffffff;
    --red: #ec1f27;
    --red-bright: #ff1a1a;
    --panel-blue: #4fb0dd;
    --field-border: #7cc6e6;
    --hero-dark: #1f5a66;
    --hero-mid: #4f8f98;
    --hero-light: #9ec7c9;
    --photo-a: #3c4a55;
    --photo-b: #8fb7c9;
  }
  * { margin: 0; padding: 0; box-sizing: border-box; }
  html, body { width: 958px; height: 1200px; overflow: hidden; background: var(--white); }
  body { position: relative; font-family: "Arimo", Arial, sans-serif; }

  .hero {
    position: absolute; left: 0; top: 0; width: 958px; height: 541px; overflow: hidden;
    background: linear-gradient(115deg, var(--hero-dark) 0%, var(--hero-mid) 45%, var(--hero-light) 100%);
  }
  .hero-nav { position: absolute; top: 27px; left: 645px; }
  .hero-nav a {
    position: absolute; white-space: nowrap; color: var(--white);
    font-weight: 700; font-size: 13px; text-decoration: none;
  }
  .brand-mark { position: absolute; display: flex; flex-direction: column; align-items: center; }
  .brand-name {
    writing-mode: vertical-rl; transform: rotate(180deg);
    color: var(--red); font-size: 14px; font-weight: 400; letter-spacing: 0.5px;
  }
  .brand-dot { width: 34px; height: 34px; border-radius: 50%; background: var(--red); margin-top: 6px; }

  .headline {
    position: absolute; left: 0; width: 958px; top: 236px; text-align: center;
    color: var(--white); font-style: italic; font-size: 48px; font-weight: 400;
  }

  .social-list { position: absolute; list-style: none; width: 50px; }
  .social-list li {
    position: absolute; left: 0; height: 18px; width: 50px;
    display: flex; align-items: center; gap: 4px;
    font-size: 10px; font-weight: 700; letter-spacing: 0.3px;
  }
  .social-list li::before {
    content: ""; width: 8px; height: 8px; border-radius: 50%; flex: none;
  }
  .hero .social-list li { color: var(--white); }
  .hero .social-list li::before { background: var(--white); }
  .page .social-list li { color: var(--red); }
  .page .social-list li::before { background: var(--red); }

  .side-email {
    position: absolute; writing-mode: vertical-rl; font-size: 12px; font-weight: 700; white-space: nowrap;
  }
  .hero .side-email { color: var(--white); }

  .slider-dots { position: absolute; top: 518px; left: 334px; }
  .slider-dots span { position: absolute; top: 0; width: 63px; height: 6px; background: rgba(255,255,255,0.85); }

  .feature-panel {
    position: absolute; left: 70px; top: 570px; width: 819px; height: 440px;
    background: var(--panel-blue);
  }
  .feature-photo { position: absolute; width: 285px; height: 306px; top: 54px; }
  .feature-photo.one { left: 56px; background: linear-gradient(160deg, var(--photo-b), var(--photo-a) 70%); }
  .feature-photo.two { left: 464px; background: linear-gradient(180deg, #9cc7e0, #5ab2c8 40%, #d9d9d9 75%, #6d7a6a); }
  .read-more {
    position: absolute; top: 378px; color: var(--red); font-variant: small-caps;
    font-size: 16px; text-decoration: underline; text-underline-offset: 3px;
  }

  .side-nav { position: absolute; left: 878px; top: 585px; width: 80px; text-align: center; }
  .side-nav a {
    position: absolute; left: 0; width: 80px; color: var(--red);
    font-style: italic; font-size: 13px; text-decoration: none;
  }
  .side-nav a.current { text-decoration: underline; }
  .page .side-email { color: var(--red); }

  .optin-field {
    position: absolute; left: 162px; top: 1105px; width: 376px; height: 39px;
    border: 1px solid var(--field-border); border-radius: 5px;
    display: flex; align-items: center; justify-content: center;
    color: var(--red); font-style: italic; font-variant: small-caps; font-size: 14px;
  }
  .optin-button {
    position: absolute; left: 571px; top: 1105px; width: 152px; height: 39px;
    background: var(--red-bright); border-radius: 4px;
    display: flex; align-items: center; justify-content: center;
    color: var(--white); font-style: italic; font-variant: small-caps; font-size: 16px;
  }
</style>
</head>
<body>
  <header class="hero" role="img" aria-label="Video slider: a presenter at a flip chart being filmed by a camera operator in a bright living room, teal tint">
    <nav class="hero-nav">
      <a style="left:0">Work</a>
      <a style="left:59px">About</a>
      <a style="left:114px">Blog</a>
      <a style="left:158px">Contacts</a>
    </nav>
    <div class="brand-mark" style="left:21px; top:30px;">
      <span class="brand-name">Karel Dumonte</span>
      <span class="brand-dot"></span>
    </div>
    <h1 class="headline">Against all odds, I will prosper</h1>
    <ul class="social-list" style="left:26px; top:385px;" aria-label="Social profiles">
      <li style="top:0">Page</li><li style="top:34px">Feed</li><li style="top:70px">Pics</li><li style="top:106px">Plus</li>
    </ul>
    <div class="side-email" style="left:914px; top:372px;">hello@dumonte.example</div>
    <div class="slider-dots">
      <span style="left:0"></span><span style="left:77px"></span><span style="left:154px"></span><span style="left:232px"></span>
    </div>
  </header>

  <main class="page">
    <div class="brand-mark" style="left:20px; top:586px;">
      <span class="brand-name">Karel Dumonte</span>
      <span class="brand-dot"></span>
    </div>
    <ul class="social-list" style="left:20px; top:861px;" aria-label="Social profiles">
      <li style="top:0">Page</li><li style="top:34px">Feed</li><li style="top:70px">Pics</li><li style="top:106px">Plus</li>
    </ul>

    <section class="feature-panel">
      <div class="feature-photo one" role="img" aria-label="Portrait of a young man in glasses and a navy polo outdoors"></div>
      <a class="read-more" style="left:268px">Read More</a>
      <div class="feature-photo two" role="img" aria-label="Young man in sunglasses and white shirt checking his phone by the sea"></div>
      <a class="read-more" style="left:674px">Read More</a>
    </section>

    <nav class="side-nav">
      <a class="current" style="top:0">Work</a>
      <a style="top:26px">About</a>
      <a style="top:52px">Blog</a>
      <a style="top:81px">Contacts</a>
    </nav>
    <div class="side-email" style="left:914px; top:886px;">hello@dumonte.example</div>

    <form class="optin">
      <div class="optin-field">Get the latest updates</div>
      <div class="optin-button">Subscribe Now</div>
    </form>
  </main>
</body>
</html>
```